Flyer for tutoring

The text should be presented in an engaging way to attract potential customers.
Colorfully designed
Around the edge, various objects related to school and the subjects (see text) should be visible.

```html
<!DOCTYPE html>
<html lang="de">
<head>
<meta charset="utf-8">
<title>Nachhilfe – Lerncoach</title>
<link href="https://fonts.googleapis.com/css2?family=Luckiest+Guy&family=Kreon:wght@400;600;700&display=swap" rel="stylesheet">
<style>
  :root{
    --paper:#fbfbfd;
    --green:#45a545;
    --navy:#2f4ca0;
    --plum:#a0407a;
    --teal:#2a8290;
    --orange:#e0600f;
    --indigo:#3f3a9a;
    --cyan:#08b2e3;
    --supply-orange:#f39a1e;
    --supply-yellow:#f6df3c;
    --supply-pink:#e84c9a;
    --supply-red:#d9262e;
    --supply-blue:#3a86d0;
    --supply-peach:#e69a85;
  }
  html,body{margin:0;padding:0;overflow:hidden;}
  body{width:846px;height:1200px;background:var(--paper);}
  .flyer{position:relative;width:846px;height:1200px;overflow:hidden;background:var(--paper);font-family:"Kreon",Georgia,serif;}
  .supplies{position:absolute;}
  .supplies--top-left{left:0;top:0;width:205px;height:215px;background:linear-gradient(150deg,var(--supply-orange),#f7b545 70%,rgba(247,181,69,0));border-bottom-right-radius:60px;}
  .supplies--left-pad{left:0;top:200px;width:85px;height:370px;background:linear-gradient(180deg,var(--supply-yellow),#f1d640);}
  .supplies--sharpener{left:200px;top:45px;width:70px;height:110px;background:var(--supply-red);border-radius:10px;transform:rotate(-12deg);}
  .supplies--top-right{right:0;top:0;width:240px;height:200px;background:radial-gradient(ellipse at 80% 20%,var(--supply-pink),rgba(232,76,154,.35) 60%,rgba(232,76,154,0) 75%);}
  .supplies--left-edge{left:0;top:580px;width:90px;height:520px;background:linear-gradient(180deg,rgba(232,120,180,.75),rgba(246,223,60,.8) 30%,rgba(58,134,208,.7) 50%,rgba(243,154,30,.85) 75%,rgba(230,154,133,.9));border-top-right-radius:40px;}
  .supplies--bottom-left{left:40px;top:940px;width:160px;height:170px;background:var(--supply-peach);border-radius:30px;transform:rotate(-8deg);opacity:.9;}
  .supplies--bottom{left:0;bottom:0;width:846px;height:110px;background:linear-gradient(90deg,rgba(90,180,230,.8),rgba(230,120,60,.7) 40%,rgba(180,60,150,.7) 55%,rgba(40,40,60,.55) 65%,rgba(58,134,208,.6) 90%);clip-path:polygon(0 30%,30% 60%,40% 10%,60% 0,75% 20%,100% 0,100% 100%,0 100%);}
  .supplies--right-pens{right:0;top:860px;width:120px;height:340px;background:linear-gradient(90deg,rgba(120,200,90,.8),rgba(240,200,40,.8) 40%,rgba(58,134,208,.85) 80%);clip-path:polygon(30% 10%,55% 0,80% 5%,100% 12%,100% 100%,0 100%);}

  .intro{position:absolute;left:0;width:846px;top:97px;margin:0;text-align:center;color:var(--green);font-weight:700;font-size:21px;line-height:20px;}
  .title{position:absolute;left:0;width:846px;top:158px;margin:0;text-align:center;font-family:"Luckiest Guy",Impact,sans-serif;font-weight:400;color:var(--navy);font-size:47px;line-height:49px;letter-spacing:1px;transform:rotate(-1.5deg);}
  .tagline{position:absolute;left:0;width:846px;top:320px;margin:0;text-align:center;font-family:"Luckiest Guy",Impact,sans-serif;color:var(--plum);font-size:22px;letter-spacing:.5px;}
  .copy{position:absolute;left:150px;margin:0;font-weight:700;font-size:21.5px;line-height:20.2px;}
  .copy--first{top:364px;width:520px;color:var(--teal);}
  .copy--second{top:523px;width:575px;color:var(--orange);}
  .copy--third{top:660px;width:570px;color:var(--plum);}
  .promise{position:absolute;left:0;width:846px;top:714px;margin:0;text-align:center;font-family:"Luckiest Guy",Impact,sans-serif;color:var(--indigo);font-size:23px;line-height:26px;letter-spacing:.5px;}
  .about{top:779px;width:560px;color:var(--plum);font-weight:600;}
  .about strong{font-weight:700;}
  .contact{position:absolute;left:249px;top:918px;margin:0;color:var(--teal);font-size:21px;line-height:26px;font-weight:600;}
  .contact strong{font-weight:700;}
  .contact p{margin:0;}
  .badge{position:absolute;left:550px;top:980px;width:252px;height:252px;border-radius:50%;background:var(--cyan);}
  .badge-text{position:absolute;left:570px;top:1038px;width:200px;margin:0;text-align:center;color:var(--indigo);font-weight:700;font-size:22px;line-height:27px;transform:rotate(8deg);}
</style>
</head>
<body>
<main class="flyer">
  <div class="supplies supplies--top-left" role="img" aria-label="Geodreieck und Schreibpapier in Orange und Gelb"></div>
  <div class="supplies supplies--left-pad" role="img" aria-label="Gelber Notizblock"></div>
  <div class="supplies supplies--sharpener" role="img" aria-label="Roter Bleistiftspitzer"></div>
  <div class="supplies supplies--top-right" role="img" aria-label="Pinke Schere und roter Buntstift"></div>
  <div class="supplies supplies--left-edge" role="img" aria-label="Kreiden, Pinsel und bunte Radiergummis"></div>
  <div class="supplies supplies--bottom-left" role="img" aria-label="Radiergummi und Gummibänder"></div>
  <div class="supplies supplies--bottom" role="img" aria-label="Filzstifte, Pinsel und Marker"></div>
  <div class="supplies supplies--right-pens" role="img" aria-label="Bleistifte und Kugelschreiber"></div>

  <p class="intro">Möchtest du dich gerne in der Schule<br>verbessern und suchst eine</p>
  <h1 class="title">Professionelle<br>Nachhilfelehrerin/<br>Lerncoach</h1>
  <p class="tagline">Dann lass es uns doch mal versuchen!</p>

  <p class="copy copy--first">Die erste Lektion – die Kennenlernlektion – dauert ca. 30 Minuten. Sie ist kostenlos. Denn wir müssen ja sicher gehen, dass wir uns verstehen und leiden können. Bei unserem ersten Treffen legen wir auch fest, woran wir arbeiten werden und wann die Nachhilfe in deine Agenda passt.</p>
  <p class="copy copy--second">Die erste Lektion – die Kennenlernlektion – dauert ca. 30 Minuten. Sie ist kostenlos. Denn wir müssen ja sicher gehen, dass wir uns verstehen und leiden können. Bei unserem ersten Treffen legen wir auch fest, woran wir arbeiten werden und wann die Nachhilfe in deine Agenda passt.</p>
  <p class="copy copy--third">Wenn der erste Eindruck stimmt, dann legen wir los, und bald schon werden</p>

  <p class="promise">Deine Motivation und<br>deine Noten besser und besser!</p>

  <p class="copy about"><strong>Zu meiner Person:</strong> Ich wohne hier in der Siedlung Lindenhof am Bachweg und bin ausgebildete und sehr erfahrene Sekundar- und Primarlehrerin in den Fächern Deutsch, Französisch, Englisch und Geschichte. (Auf Wunsch auch Mathe-Nachhilfe möglich.)</p>

  <div class="contact">
    <p><strong>Meine Kontaktdaten:</strong></p>
    <p><strong>Mail:</strong></p>
    <p>lernen.mit.lena@postmail.ch</p>
    <p style="margin-top:6px"><strong>Tel.</strong> 079 512 47 18</p>
    <p>(nachmittags fast immer<br>erreichbar)</p>
  </div>

  <div class="badge"></div>
  <p class="badge-text">Ich freue mich auf deine Kontaktaufnahme! Bis bald!</p>
</main>
</body>
</html>
```